Card Design

We are looking for a mailing for a small business that is helping other small businesses conform to new provincial legislation regarding accessibility in the workplace.
The size will be 4" x 6"
This will be mass mailed through the post office so there is no need to included space for recipient address.
Front/Style: Professional/Official
Text:
As of right now, all businesses in Ontario that employ ONE OR MORE people, must comply with the Workplace Fairness for Residents with Mobility Statute. INCLUDING MANATORY STAFF TRAINING. (You can include an image if works with the overall look).
- We are trying to convey the idea that they need to act now.
Back
Font / Style: Professional but less official than the front.
Text:
Compliance Checklist
(please put a small box in front of each * sign)
Does your company employ ONE or more business
* Yes * No
If yes, then as of January 1,2012, your business must:
* Establish accessibility policies, practicesn and procedures
* Allow guide dogs, service animals and/or support persons onto the premises.
*Provide notice of temporary disruptions facilities and services.
*Provide training to staff.
* Establish a process for receiving and responding to accessibility feedback.
* Documentation must be kept on file
*Annual Accessibility report to the Ministry.
GET COMPLIANT NOW
Brightpath Advisory has produced a *Assured Standards Toolbox Pack to help business to become compliant with the Openness Code for Client Relations.
Contact us at
1-877-5319074 (WFRS)
email : info@brightpathadvisory.example
or brightpathadvisory.example
Industry/Entity Type
Small Business
Look and feel
Each slider illustrates characteristics of the customer's brand and the style your logo design should communicate.

```html
<!DOCTYPE html>
<html lang="en">
<head>
<meta charset="utf-8">
<title>Compliance Checklist – Brightpath Advisory</title>
<link href="https://fonts.googleapis.com/css2?family=Arimo:wght@400;700&display=swap" rel="stylesheet">
<style>
  :root {
    --page: #ffffff;
    --frame: #8a1c1c;
    --frame-ring: #c9a35f;
    --panel-light: #fcf5dc;
    --panel-dark: #e6cd8e;
    --ink: #1e1e1e;
    --brand: #c8202a;
    --box: #ffffff;
  }
  html, body {
    margin: 0;
    padding: 0;
    width: 1200px;
    height: 867px;
    overflow: hidden;
    background: var(--page);
  }
  .card {
    position: relative;
    width: 1200px;
    height: 867px;
    font-family: "Arimo", Arial, sans-serif;
    color: var(--ink);
  }
  .card-frame {
    position: absolute;
    left: 0;
    top: 0;
  }
  .content {
    position: absolute;
    inset: 0;
  }
  .title {
    position: absolute;
    left: 98px;
    top: 148px;
    margin: 0;
    font-size: 44px;
    font-weight: 700;
    letter-spacing: -0.3px;
  }
  .line {
    position: absolute;
    left: 98px;
    margin: 0;
    font-size: 17px;
    font-weight: 700;
    white-space: nowrap;
  }
  .question { top: 212px; }
  .answers { top: 244px; display: flex; align-items: center; gap: 10px; }
  .intro { top: 306px; }
  .box {
    display: inline-block;
    width: 38px;
    height: 24px;
    background: var(--box);
    vertical-align: middle;
  }
  .checklist {
    position: absolute;
    left: 98px;
    top: 356px;
    margin: 0;
    padding: 0;
    list-style: none;
  }
  .checklist li {
    display: flex;
    align-items: center;
    height: 28.5px;
    font-size: 17px;
    font-weight: 700;
    white-space: nowrap;
  }
  .checklist .star { width: 26px; }
  .checklist .box { margin-right: 23px; }
  .cta-heading { top: 592px; }
  .cta-body {
    position: absolute;
    left: 98px;
    top: 628px;
    width: 1000px;
    margin: 0;
    font-size: 17px;
    font-weight: 700;
    line-height: 39px;
  }
  .contact {
    position: absolute;
    left: 0;
    right: 0;
    top: 736px;
    margin: 0;
    text-align: center;
    font-size: 19px;
    font-weight: 400;
  }
  .brand-name {
    position: absolute;
    left: 870px;
    top: 250px;
    width: 260px;
    margin: 0;
    text-align: center;
    color: var(--brand);
    font-weight: 400;
    line-height: 1.05;
  }
  .brand-name .primary { display: block; font-size: 40px; }
  .brand-name .secondary { display: block; font-size: 28px; }
</style>
</head>
<body>
<div class="card">
  <svg class="card-frame" width="1200" height="867" viewBox="0 0 1200 867" aria-hidden="true">
    <defs>
      <radialGradient id="panelFill" cx="50%" cy="45%" r="65%">
        <stop offset="0%" stop-color="var(--panel-light)"/>
        <stop offset="60%" stop-color="#f5e6b6"/>
        <stop offset="100%" stop-color="var(--panel-dark)"/>
      </radialGradient>
    </defs>
    <rect x="50" y="50" width="1112" height="764" rx="18" fill="var(--frame)"/>
    <rect x="68" y="68" width="1076" height="728" fill="url(#panelFill)"/>
    <g fill="var(--frame)" stroke="var(--frame-ring)" stroke-width="4">
      <circle cx="96" cy="96" r="24"/>
      <circle cx="1116" cy="96" r="24"/>
      <circle cx="96" cy="768" r="24"/>
      <circle cx="1116" cy="768" r="24"/>
    </g>
  </svg>

  <div class="content">
    <h1 class="title">Compliance Checklist</h1>

    <p class="line question">Does your company employ ONE or more business</p>
    <p class="line answers">* Yes <span class="box"></span> * No <span class="box"></span></p>

    <p class="line intro">If yes, then as of January 1,2012, your business must:</p>

    <ul class="checklist">
      <li><span class="star">*</span><span class="box"></span>Establish accessibility policies, practicesn and procedures</li>
      <li><span class="star">*</span><span class="box"></span>Allow guide dogs, service animals and/or support persons onto the premises.</li>
      <li><span class="star">*</span><span class="box"></span>Provide notice of temporary disruptions facilities and services.</li>
      <li><span class="star">*</span><span class="box"></span>Provide training to staff.</li>
      <li><span class="star">*</span><span class="box"></span>Establish a process for receiving and responding to accessibility feedback.</li>
      <li><span class="star">*</span><span class="box"></span>Documentation must be kept on file</li>
      <li><span class="star">*</span><span class="box"></span>Annual Accessibility report to the Ministry.</li>
    </ul>

    <p class="line cta-heading">GET COMPLIANT NOW</p>
    <p class="cta-body">Brightpath Advisory has produced a *Assured Standards Toolbox Pack to help business to become compliant with the Openness Code for Client Relations.</p>

    <p class="contact">1-877-5319074 (WFRS) &nbsp;|&nbsp; info@brightpathadvisory.example &nbsp;|&nbsp; brightpathadvisory.example</p>

    <p class="brand-name"><span class="primary">BRIGHTPATH</span><span class="secondary">ADVISORY INC.</span></p>
  </div>
</div>
</body>
</html>
```